Plakat-Design für Immobilienmakler
Zielgruppe
Wir sind Immobilienmakler
Aufgabenstellung
Benötigen die Datei für eine Schaufenstervollbeklebung.
Maße: Bx 1,99m, H 1,70m
Ist direkt in der Stadt an der Straße.
Soll schick, edel aussehen und unsere Leistungen aufzeigen.
z.B.
Lehnen Sie sich zurück wir kümmern uns um Ihre Immobilie!
oder
Wir haben den passenden Käufer für Ihre Immobilie!
- kaufen
- verkaufen
- makeln
- Home Staging
- Hausmeisterservice
Ihr Immobilienmakler in Gaildorf, Schwäbisch Hall, Backnang

```html
<!DOCTYPE html>
<html lang="de">
<head>
<meta charset="utf-8">
<title>Tallberg Immobilien – Schaufenster</title>
<link href="https://fonts.googleapis.com/css2?family=Roboto:wght@400;500;700&display=swap" rel="stylesheet">
<style>
  :root {
    --concrete-light: #a3a3a3;
    --concrete-mid: #8f8f8f;
    --concrete-dark: #7a7a7a;
    --white: #ffffff;
    --gold: #b8913f;
    --gold-light: #d2ae62;
    --gold-dark: #a88434;
    --ink: #2a2a2a;
    --suit: #1c1c1c;
  }
  * { margin: 0; padding: 0; box-sizing: border-box; }
  html, body { width: 1200px; height: 1025px; overflow: hidden; }
  body { font-family: "Roboto", Arial, sans-serif; }
  .poster {
    position: relative;
    width: 1200px;
    height: 1025px;
    overflow: hidden;
    background: radial-gradient(ellipse at 45% 40%, var(--concrete-light), var(--concrete-mid) 55%, var(--concrete-dark));
    color: var(--white);
  }
  .headline {
    position: absolute;
    left: 50px;
    top: 40px;
    font-weight: 700;
    font-size: 100px;
    line-height: 112px;
    letter-spacing: 0.5px;
  }
  .values {
    position: absolute;
    left: 50px;
    top: 284px;
    list-style: none;
    font-size: 51px;
    line-height: 59px;
    font-weight: 400;
  }
  .values li { display: flex; align-items: center; gap: 18px; }
  .values svg { width: 50px; height: 40px; }
  .team-photo {
    position: absolute;
    left: 524px;
    top: 245px;
    width: 636px;
    height: 725px;
    background: linear-gradient(180deg, rgba(40,40,40,0.15) 0%, rgba(28,28,28,0.85) 35%, var(--suit) 100%);
    border-radius: 160px 160px 0 0;
  }
  .services {
    position: absolute;
    left: 0;
    top: 546px;
    width: 380px;
  }
  .services-title {
    background: var(--white);
    color: var(--gold);
    font-weight: 700;
    font-size: 33px;
    height: 61px;
    line-height: 61px;
    padding-left: 39px;
    border-top-right-radius: 12px;
  }
  .services-list {
    list-style: none;
    background: linear-gradient(90deg, var(--gold-light), var(--gold));
    padding: 12px 0 14px 38px;
    font-size: 32px;
    line-height: 38px;
    border-bottom-right-radius: 12px;
  }
  .services-list li::before { content: "• "; }
  .region {
    position: absolute;
    left: 36px;
    top: 883px;
    font-size: 25px;
    line-height: 31px;
  }
  .footer-band {
    position: absolute;
    left: 0;
    top: 968px;
    width: 1200px;
    height: 57px;
    background: linear-gradient(90deg, var(--gold-light), var(--gold) 60%, var(--gold-dark));
    border-top: 2px solid var(--white);
  }
  .website {
    position: absolute;
    right: 77px;
    top: 7px;
    font-size: 35px;
    font-weight: 400;
  }
  .brand {
    position: absolute;
    left: 832px;
    top: 0;
    width: 298px;
    height: 192px;
    background: var(--white);
    border-radius: 0 0 14px 14px;
    display: flex;
    align-items: center;
    justify-content: center;
  }
  .brand-name {
    color: var(--ink);
    font-weight: 700;
    font-size: 34px;
    line-height: 40px;
    text-align: center;
  }
</style>
</head>
<body>
<main class="poster">
  <h1 class="headline">Wofür wir<br>(hier) stehen?</h1>

  <ul class="values">
    <li>- Seriösität <svg viewBox="0 0 50 40"><polyline points="4,20 18,34 46,4" fill="none" stroke="#fff" stroke-width="3.5"/></svg></li>
    <li>- Engagement <svg viewBox="0 0 50 40"><polyline points="4,20 18,34 46,4" fill="none" stroke="#fff" stroke-width="3.5"/></svg></li>
    <li>- Erfahrung <svg viewBox="0 0 50 40"><polyline points="4,20 18,34 46,4" fill="none" stroke="#fff" stroke-width="3.5"/></svg></li>
  </ul>

  <div class="team-photo" role="img" aria-label="Foto des Maklerteams: eine Frau und ein Mann in dunklen Anzügen vor einer Betonwand"></div>

  <section class="services">
    <h2 class="services-title">Unsere Leistungen</h2>
    <ul class="services-list">
      <li>kaufen</li>
      <li>verkaufen</li>
      <li>makeln</li>
      <li>Home Staging</li>
      <li>Hausmeisterservice</li>
    </ul>
  </section>

  <p class="region">Ihr Immobilienmakler<br>in Gaildorf, Schwäbisch Hall, Backnang</p>

  <div class="brand">
    <span class="brand-name">Tallberg<br>Immobilien</span>
  </div>

  <footer class="footer-band">
    <span class="website">www.tallberg-immobilien.de</span>
  </footer>
</main>
</body>
</html>
```